Animal Horse & Bedding Company Needs a Website Coded & Designed

We need a website for a new animal bedding and feed company that is visually grabbing and vibrant. We would like to see a website that displays trust, quality and confidence. Needs to be responsive and mobile friendly for all browsers and coded for both Android & IOS. SEO is also important.

Joomla or Wordpress – must be both desktop and mobile friendly with fast page load speed. Need the ability to edit ourselves in Wordpress or Joomla.

Full details attached below with some layout and content ideas.

Coding

Coded - Design and coding required

Number of Pages Required

5+ page

Font styles to use
Sans Serif

Requirements
Must have
• Needs to be responsive and mobile friendly for all browsers and coded for both Android & IOS. SEO is also important.

Wordpress – must be both desktop and mobile friendly with fast page load speed. Need the ability to edit ourselves in Wordpress.

Logo Colours:
Dark Brown
CMYK: 50 / 70 / 80 / 70
Pantone: 4625C

Orange
CMYK: 0 / 50 / 100 / 0
Pantone: 144C
Nice to have
• Use picture of building attached and super impose logo on building.

```html
<!DOCTYPE html>
<html lang="en">
<head>
<meta charset="utf-8">
<title>Harvest Bale Bedding &amp; Feed</title>
<link rel="stylesheet" href="https://fonts.googleapis.com/css2?family=Arimo:wght@400;700&family=Lato:wght@400;700&display=swap">
<style>
:root{
  --orange:#f7941d;
  --brown:#3b2416;
  --ink:#1a1a1a;
  --body:#333;
  --footer:#2b2b2b;
  --white:#fff;
  --head:'Arimo',Arial,sans-serif;
  --text:'Lato',Arial,sans-serif;
}
*{box-sizing:border-box;margin:0;padding:0}
html,body{width:1200px;height:2586px;overflow:hidden;background:var(--white)}
body{position:relative;font-family:var(--text);color:var(--body)}
a{color:inherit;text-decoration:none}

.topbar{position:absolute;top:0;left:0;width:1200px;height:54px;background:var(--orange);color:var(--white);font-family:var(--head);font-size:17px}
.topbar .socials{position:absolute;left:86px;top:18px;display:flex;gap:13px}
.topbar .socials span{width:15px;height:15px;border:2px solid var(--white);border-radius:3px}
.topbar .contact{position:absolute;right:90px;top:10px;display:flex;align-items:center;gap:34px}
.topbar .contact div{display:flex;align-items:center;gap:10px}
.round-icon{width:32px;height:32px;border-radius:50%;background:var(--white);display:flex;align-items:center;justify-content:center}

.nav{position:absolute;top:54px;left:0;width:1200px;height:124px;background:var(--white)}
.brand{position:absolute;left:88px;top:46px;font-family:var(--head);font-weight:700;font-size:21px;color:var(--brown);line-height:1.1}
.brand small{display:block;font-size:9px;letter-spacing:5px;color:var(--brown);font-weight:700}
.nav ul{position:absolute;left:300px;top:48px;display:flex;gap:53px;list-style:none;font-family:var(--head);font-weight:700;font-size:18px;color:var(--ink)}
.btn{display:inline-block;background:var(--brown);color:var(--white);font-family:var(--head);font-weight:700;font-size:18px}
.nav .btn{position:absolute;left:936px;top:32px;width:179px;height:53px;line-height:53px;text-align:center}

.hero{position:absolute;top:178px;left:0;width:1200px;height:600px;background:linear-gradient(100deg,#7a5a1a 0%,#b07a22 30%,#8a6020 55%,#3a2a14 75%,#6a4a1a 100%)}
.hero .photo{position:absolute;inset:0}
.hero h1{position:absolute;left:83px;top:166px;font-family:var(--head);font-weight:700;font-size:46px;line-height:52px;color:var(--white)}
.hero p{position:absolute;left:83px;top:276px;font-size:27px;line-height:31px;color:var(--white)}
.hero .btn{position:absolute;left:84px;top:372px;width:151px;height:55px;line-height:55px;text-align:center}
.hero .arrow{position:absolute;top:284px}

.features{position:absolute;top:718px;left:92px;display:flex;gap:30px}
.feature{width:318px;height:172px;background:var(--white);border:1px solid var(--orange);text-align:center;font-family:var(--head);font-weight:700;font-size:18px;color:var(--ink);padding-top:34px}
.feature svg{display:block;margin:0 auto 14px}
.feature.active{background:var(--orange);color:var(--white)}

.about-art{position:absolute;left:160px;top:920px;width:300px;height:405px;border-radius:150px 150px 150px 150px/120px 120px 180px 180px;background:linear-gradient(180deg,#c9d3dd,#8a8f94 50%,#5a4a44)}
.about{position:absolute;left:548px;top:985px;width:490px}
.about h2{font-family:var(--head);font-weight:700;font-size:40px;color:var(--ink);margin-bottom:30px}
.about p{font-size:15.5px;line-height:30px;color:var(--body)}
.about .btn{margin-top:34px;width:165px;height:55px;line-height:55px;text-align:center}

.services{position:absolute;top:1414px;left:0;width:1200px;height:408px;display:flex}
.service{width:600px;height:408px;text-align:center;color:var(--white);padding-top:52px}
.service.bedding{background:linear-gradient(135deg,#f08f17,#f7a030 50%,#f3931b)}
.service.feed{background:linear-gradient(135deg,#4a2e20,#5e3a26 50%,#3e271c)}
.service .pic{width:90px;height:90px;margin:0 auto;border-radius:50%;background:rgba(255,255,255,.25)}
.service h3{font-family:var(--head);font-weight:700;font-size:27px;margin:26px 0 18px}
.service ul{list-style:none;font-size:16px;line-height:38px}
.service li::before{content:"";display:inline-block;width:8px;height:8px;border:2px solid var(--white);border-radius:50%;margin-right:9px;vertical-align:1px}
.service .more{display:inline-block;margin-top:14px;font-family:var(--head);font-weight:700;font-size:18px}
.service .more::after{content:"›";display:inline-block;width:15px;height:15px;line-height:14px;margin-left:18px;border-radius:50%;background:var(--white);font-size:14px;color:var(--orange)}
.service.feed .more::after{color:var(--brown)}

.newsletter{position:absolute;top:1895px;left:0;width:1200px;text-align:center}
.newsletter h2{font-family:var(--head);font-weight:700;font-size:41px;color:var(--ink)}
.newsletter .field{width:335px;height:45px;margin:22px auto 0;border:1px solid #777;text-align:left;padding:12px 9px;font-size:15px;color:var(--body)}
.newsletter .btn{margin-top:22px;width:145px;height:47px;line-height:47px}

.footer{position:absolute;top:2165px;left:0;width:1200px;height:421px;background:var(--footer);color:var(--white)}
.footer .brand{left:86px;top:150px;color:var(--white);font-size:27px}
.footer .brand small{color:var(--white);font-size:11px;letter-spacing:8px}
.col{position:absolute;top:54px}
.col h4{font-family:var(--head);font-weight:400;font-size:17px;margin-bottom:20px}
.col li{list-style:none;font-size:15px;display:flex;align-items:center;gap:10px}
.follow{left:378px}.follow li{height:44px}
.follow .dot{width:30px;height:30px;border-radius:50%;background:var(--orange)}
.info{left:623px}.info li{height:39px}
.reach{left:829px}.reach li{font-family:var(--head);font-size:17px;gap:12px;margin-bottom:32px;align-items:flex-start;line-height:25px}
.reach .round-icon{background:var(--orange);flex:none}
.footer hr{position:absolute;left:86px;top:330px;width:1029px;border:0;border-top:1px solid #666}
.copy{position:absolute;top:375px;width:1200px;text-align:center;font-size:15px}
</style>
</head>
<body>

<header class="topbar">
  <div class="socials"><span></span><span></span><span></span><span></span></div>
  <div class="contact">
    <div><span class="round-icon"><svg width="16" height="12" viewBox="0 0 16 12"><rect x="1" y="1" width="14" height="10" fill="none" stroke="#f7941d" stroke-width="1.5"/><path d="M1 1l7 6 7-6" fill="none" stroke="#f7941d" stroke-width="1.5"/></svg></span>info@harvestbalebedding.com</div>
    <div><span class="round-icon"><svg width="14" height="14" viewBox="0 0 24 24"><path d="M6.6 10.8a15 15 0 006.6 6.6l2.2-2.2c.3-.3.7-.4 1-.2 1.1.4 2.3.6 3.6.6.6 0 1 .4 1 1V20c0 .6-.4 1-1 1A17 17 0 013 4c0-.6.4-1 1-1h3.5c.6 0 1 .4 1 1 0 1.3.2 2.5.6 3.6.1.3 0 .7-.2 1z" fill="#f7941d"/></svg></span>(123) 456 789</div>
  </div>
</header>

<nav class="nav">
  <div class="brand">HARVEST BALE<small>BEDDING &amp; FEED</small></div>
  <ul><li>HOME</li><li>ABOUT US</li><li>FEED</li><li>BEDDING</li><li>CONTACT US</li></ul>
  <a class="btn">REQUEST QUOTE</a>
</nav>

<section class="hero">
  <div class="photo" role="img" aria-label="Woman greeting a dark horse in a sunlit meadow"></div>
  <h1>HARVEST BALE<br>BEDDING &amp;FEED</h1>
  <p>Grown for quality - 100% natural with<br>no chemicals or additives</p>
  <a class="btn">GET STARTED</a>
  <svg class="arrow" style="left:38px" width="18" height="28" viewBox="0 0 18 28"><path d="M14 3L4 14l10 11" fill="none" stroke="#fff" stroke-width="3"/></svg>
  <svg class="arrow" style="left:1143px" width="18" height="28" viewBox="0 0 18 28"><path d="M4 3l10 11L4 25" fill="none" stroke="#fff" stroke-width="3"/></svg>
</section>

<div class="features">
  <div class="feature">
    <svg width="72" height="70" viewBox="0 0 72 70"><path d="M32 4l24 9v18c0 17-11 28-24 34C19 59 8 48 8 31V13z" fill="none" stroke="#a0521a" stroke-width="2.5"/><circle cx="50" cy="50" r="14" fill="#f7941d"/><path d="M43 50l5 5 9-10" fill="none" stroke="#fff" stroke-width="3"/></svg>
    QUALITY GUARANTEED
  </div>
  <div class="feature active">
    <svg width="72" height="70" viewBox="0 0 72 70"><circle cx="26" cy="34" r="10" fill="none" stroke="#fff" stroke-width="2.5"/><path d="M8 66c0-12 8-18 18-18s18 6 18 18" fill="none" stroke="#fff" stroke-width="2.5"/><rect x="40" y="4" width="26" height="18" rx="3" fill="none" stroke="#fff" stroke-width="2.5"/><path d="M46 22l-4 7 9-7" fill="none" stroke="#fff" stroke-width="2.5"/></svg>
    FULL SERVICE SOLUTION
  </div>
  <div class="feature">
    <svg width="80" height="74" viewBox="0 0 80 74"><path d="M20 22c-12 8-14 30-4 40h24c8-10 6-32-6-40z" fill="none" stroke="#a0521a" stroke-width="2.5"/><circle cx="30" cy="56" r="11" fill="#f7941d"/><rect x="46" y="40" width="6" height="30" fill="#a0521a"/><rect x="56" y="30" width="6" height="40" fill="#a0521a"/><rect x="66" y="20" width="6" height="50" fill="#a0521a"/><path d="M62 14V2m-4 4l4-4 4 4" fill="none" stroke="#a0521a" stroke-width="2"/></svg>
    COST EFFECTIVE
  </div>
</div>

<div class="about-art" role="img" aria-label="Farm buildings and fields seen through a horseshoe shape"></div>
<section class="about">
  <h2>ABOUT US</h2>
  <p>Harvest Bale is a locally owned company located in Pinecrest, AB.&nbsp; We are dedicated in providing high quality products and services. Producing, buying and marketing hay and straw for x amount of years. Insert blub on ownership/history of key staff/owners.</p>
  <a class="btn">LEARN MORE</a>
</section>

<section class="services">
  <div class="service bedding" role="img" aria-label="Rabbit resting on golden straw">
    <div class="pic"></div>
    <h3>BEDDING</h3>
    <ul><li>100% Natural Chopped Straw</li><li>Economic – less used and less wasted</li><li>Cheaper than Wood Shavings</li></ul>
    <a class="more">READ MORE</a>
  </div>
  <div class="service feed" role="img" aria-label="Horses standing in a field">
    <div class="pic"></div>
    <h3>FEED</h3>
    <ul><li>Chemical &amp; Additive Free</li><li>Available in Pellets or Cubes</li><li>Eliminate Waste In Feeding</li></ul>
    <a class="more">READ MORE</a>
  </div>
</section>

<section class="newsletter">
  <h2>NEWSLETTER</h2>
  <div class="field">Enter Your Email:</div>
  <a class="btn">SUBSCRIBE</a>
</section>

<footer class="footer">
  <div class="brand">HARVEST BALE<small>BEDDING &amp; FEED</small></div>
  <div class="col follow"><h4>Follows Us</h4><ul><li><span class="dot"></span>Chatter</li><li><span class="dot"></span>Chirp</li><li><span class="dot"></span>Worklink</li><li><span class="dot"></span>Pinboard</li></ul></div>
  <div class="col info"><h4>Information</h4><ul><li>Home</li><li>About Us</li><li>Feed</li><li>Bedding</li><li>Contact us</li></ul></div>
  <div class="col reach"><h4>Contact us</h4><ul>
    <li><span class="round-icon"><svg width="14" height="14" viewBox="0 0 24 24"><path d="M6.6 10.8a15 15 0 006.6 6.6l2.2-2.2c.3-.3.7-.4 1-.2 1.1.4 2.3.6 3.6.6.6 0 1 .4 1 1V20c0 .6-.4 1-1 1A17 17 0 013 4c0-.6.4-1 1-1h3.5c.6 0 1 .4 1 1 0 1.3.2 2.5.6 3.6.1.3 0 .7-.2 1z" fill="#fff"/></svg></span>(123) 456 789</li>
    <li><span class="round-icon"><svg width="16" height="12" viewBox="0 0 16 12"><rect x="1" y="1" width="14" height="10" fill="none" stroke="#fff" stroke-width="1.5"/><path d="M1 1l7 6 7-6" fill="none" stroke="#fff" stroke-width="1.5"/></svg></span>hello@harvestbale.com</li>
    <li><span class="round-icon"><svg width="12" height="16" viewBox="0 0 12 16"><path d="M6 15S1 9 1 6a5 5 0 0110 0c0 3-5 9-5 9z" fill="none" stroke="#fff" stroke-width="1.5"/><circle cx="6" cy="6" r="1.8" fill="#fff"/></svg></span>11,3Lorem ipsum dolor sit amet<br>consectetur adipiscing elit</li>
  </ul></div>
  <hr>
  <p class="copy">©Copyright 2021 Harvest Bale Bedding feed.All right reserved.</p>
</footer>

</body>
</html>
```